Design a book cover for "The Ledgerkeeper's Yarn"

We need a book cover for a book titled "The Ledgerkeeper's Yarn" The subtitle is "How Machines Permit a Shared Dividend, the Close of Wage Levies, and an Even Treasury"
You can use one of the attached files of cover art, or come up with your own art - designer's choice!
Author's Name is Derek Halvorn
We'd like the copy in the attached file "Back Cover" on the back cover, along with the copy in "About the Author" and the author's photo on the back cover.
Updates

Project Deadline Extended Reason: The deadline has been extended to give time for designers to respond to comments. Feel free to submit designs that do not use the cover art graphics attached to the brief - that art was meant as a suggestion. Added Sunday, January 15, 2017

Target Market(s)

Layperson

Font styles to use
Sans Serif

Colors
0456a4
3176b5
85abd2
0293ce
33a6d7
85cae6
1b1b1b
474747
919191

Requirements
Nice to have
• We'd like to see how the horse and rider would look on the front cover. The attached file, "Wendlow Option", is a rough sketch. The artist is refining it, adding color, and will have the rider carrying modern technology instead of scrolls.
• We are open to all colors, but have indicated some colors we like.

```html
<!DOCTYPE html>
<html lang="en">
<head>
<meta charset="utf-8">
<title>The Ledgerkeeper's Yarn — Book Cover</title>
<link href="https://fonts.googleapis.com/css2?family=Arvo:wght@700&family=Raleway:wght@400;500&display=swap" rel="stylesheet">
<style>
  :root {
    --page-bg: #eef0f3;
    --sky-top: #172238;
    --sky-mid: #34507a;
    --sky-low: #5a7fa3;
    --sky-bottom: #4fa6b4;
    --title-ink: #ffffff;
    --subtitle-ink: #c3cbd8;
    --author-ink: #d9e4ec;
    --art-glow: rgba(226, 238, 246, 0.78);
    --art-mint: rgba(150, 210, 200, 0.55);
    --art-note: rgba(92, 170, 120, 0.55);
    --art-edge: rgba(120, 160, 190, 0);
  }
  * { box-sizing: border-box; margin: 0; padding: 0; }
  html, body {
    width: 1200px;
    height: 926px;
    overflow: hidden;
    background: var(--page-bg);
  }
  .stage {
    width: 1200px;
    height: 926px;
    display: flex;
    align-items: center;
    justify-content: center;
  }
  .cover {
    position: relative;
    width: 540px;
    height: 808px;
    background: linear-gradient(180deg,
      var(--sky-top) 0%,
      var(--sky-top) 18%,
      var(--sky-mid) 48%,
      var(--sky-low) 72%,
      var(--sky-bottom) 100%);
    overflow: hidden;
    text-align: center;
    box-shadow: 0 6px 24px rgba(0, 0, 0, 0.18);
  }
  .cover__title {
    position: absolute;
    top: 78px;
    left: 0;
    right: 0;
    color: var(--title-ink);
    font-family: "Arvo", "Rockwell", serif;
    font-weight: 700;
    line-height: 1;
  }
  .cover__title-article {
    display: block;
    font-size: 20px;
    letter-spacing: 3px;
    margin-bottom: 6px;
  }
  .cover__title-main {
    display: block;
    font-size: 50px;
    line-height: 1.08;
    letter-spacing: -0.5px;
  }
  .cover__subtitle {
    position: absolute;
    top: 240px;
    left: 78px;
    right: 78px;
    color: var(--subtitle-ink);
    font-family: "Raleway", sans-serif;
    font-weight: 400;
    font-size: 20px;
    line-height: 1.2;
  }
  .cover__art {
    position: absolute;
    top: 334px;
    left: 72px;
    width: 396px;
    height: 360px;
    border-radius: 40px;
    background: radial-gradient(ellipse 60% 55% at 50% 50%,
      var(--art-glow) 0%,
      var(--art-mint) 45%,
      var(--art-note) 68%,
      var(--art-edge) 100%);
  }
  .cover__author {
    position: absolute;
    bottom: 52px;
    left: 0;
    right: 0;
    color: var(--author-ink);
    font-family: "Raleway", sans-serif;
    font-weight: 500;
    font-size: 23px;
    letter-spacing: 4px;
  }
</style>
</head>
<body>
  <main class="stage">
    <article class="cover">
      <h1 class="cover__title">
        <span class="cover__title-article">THE</span>
        <span class="cover__title-main">Ledgerkeeper's<br>Yarn</span>
      </h1>
      <p class="cover__subtitle">How Machines Permit a Shared Dividend, the Close of Wage Levies, and an Even Treasury</p>
      <div class="cover__art" role="img" aria-label="Central illustration: a hand-drawn glowing cloud linked by circuit lines to three green dollar notes above and to connector pins below"></div>
      <p class="cover__author">Derek Halvorn</p>
    </article>
  </main>
</body>
</html>
```